Business card design needed

i need a business card designed for my hair salon its call parlour 71 i want the cards to look similar to the velvet 88 design a big 71 with studio written in the top part of the 3.The 71 big on the left side then all my details (number address name) would love it to be a vintage look, colours to be in black and white/silver card to b black.
to have a line on the back with appointment day time, also would love a vip card like the vip drink card but with free treatments or shampoo so five visits that can b stamped and get a free treatment then 10th get 10% off... or something like that...
Industry/Entity Type
Hair
Contact Information for Business Card
Parlour 71
Mira Dunwoody
0431279406
71 Orchard Crescent, Tallow Bend

```html
<!DOCTYPE html>
<html lang="en">
<head>
<meta charset="utf-8">
<title>Parlour 71 – Business Card</title>
<link href="https://fonts.googleapis.com/css2?family=Open+Sans:wght@400;600;700&display=swap" rel="stylesheet">
<style>
  :root {
    --page-bg: #f3f3f3;
    --card-black: #111111;
    --card-deep: #1c1c1c;
    --damask-light: #3a3a3a;
    --damask-dark: #161616;
    --silver: #9a9a9a;
    --silver-light: #bdbdbd;
    --ink-white: #ffffff;
    --ink-soft: #dadada;
  }
  * { margin: 0; padding: 0; box-sizing: border-box; }
  html, body {
    width: 1200px;
    height: 900px;
    overflow: hidden;
    background: var(--page-bg);
    font-family: "Open Sans", sans-serif;
  }
  .canvas {
    position: relative;
    width: 1200px;
    height: 900px;
  }
  .card {
    position: absolute;
    top: 300px;
    width: 520px;
    height: 310px;
    border-radius: 24px;
    overflow: hidden;
    background: var(--card-black);
    box-shadow: 0 18px 30px rgba(0,0,0,0.18);
  }
  .card--back { left: 60px; }
  .card--front { left: 620px; }
  .card__art {
    position: absolute;
    inset: 0;
    width: 100%;
    height: 100%;
  }
  .card__content {
    position: absolute;
    inset: 0;
    color: var(--ink-white);
  }

  /* Appointment side */
  .appointments__title {
    position: absolute;
    top: 40px;
    left: 0;
    width: 100%;
    padding-left: 10px;
    text-align: center;
    font-size: 20px;
    font-weight: 400;
    letter-spacing: 6px;
  }
  .field-label {
    position: absolute;
    font-size: 17px;
    color: var(--ink-white);
  }
  .field-box {
    position: absolute;
    height: 34px;
    background: var(--ink-white);
  }
  .label-name { left: 18px; top: 100px; }
  .box-name { left: 82px; top: 96px; width: 412px; }
  .label-date { left: 18px; top: 160px; }
  .box-date { left: 82px; top: 156px; width: 150px; }
  .label-time { left: 238px; top: 160px; }
  .box-time { left: 300px; top: 156px; width: 194px; }

  .stamp-row {
    position: absolute;
    left: 124px;
    display: flex;
    align-items: center;
    gap: 3px;
  }
  .stamp-row--first { top: 206px; }
  .stamp-row--second { top: 242px; }
  .stamp {
    width: 30px;
    height: 30px;
    border-radius: 50%;
    background: var(--ink-white);
  }
  .stamp-row__reward {
    margin-left: 6px;
    font-size: 20px;
    color: var(--ink-white);
  }

  /* Details side */
  .brand-name {
    position: absolute;
    top: 88px;
    left: 0;
    width: 100%;
    padding-left: 50px;
    text-align: center;
    font-size: 48px;
    font-weight: 700;
    color: var(--ink-white);
    letter-spacing: 2px;
  }
  .contact {
    position: absolute;
    top: 196px;
    left: 0;
    width: 100%;
    padding-left: 40px;
    text-align: center;
    color: var(--ink-soft);
    line-height: 1.25;
  }
  .contact__name { font-size: 19px; }
  .contact__phone { font-size: 15px; }
  .contact__address { font-size: 16px; color: var(--ink-white); }
</style>
</head>
<body>
<main class="canvas">

  <section class="card card--back" aria-label="Appointment and loyalty side">
    <svg class="card__art" viewBox="0 0 520 310" preserveAspectRatio="none" aria-hidden="false">
      <defs>
        <radialGradient id="damaskBack" cx="50%" cy="45%" r="60%">
          <stop offset="0" stop-color="var(--damask-light)"/>
          <stop offset="1" stop-color="var(--damask-dark)"/>
        </radialGradient>
      </defs>
      <rect x="0" y="0" width="520" height="310" fill="url(#damaskBack)" role="img" aria-label="Dark vintage damask pattern"/>
      <path d="M0,0 L230,0 C140,0 60,14 0,34 Z" fill="var(--card-black)"/>
      <path d="M0,62 C80,30 180,24 290,24 C330,24 345,0 380,0 L230,0 C140,0 60,14 0,34 Z" fill="var(--silver)"/>
      <path d="M0,300 C60,270 150,262 260,262 C360,262 440,250 520,200 L520,232 C450,280 380,290 300,310 L0,310 Z" fill="var(--silver)"/>
      <path d="M300,310 C380,290 450,280 520,232 L520,310 Z" fill="var(--card-black)"/>
    </svg>
    <div class="card__content">
      <h2 class="appointments__title">Appointments</h2>
      <span class="field-label label-name">Name :</span>
      <div class="field-box box-name"></div>
      <span class="field-label label-date">Date :</span>
      <div class="field-box box-date"></div>
      <span class="field-label label-time">Time:</span>
      <div class="field-box box-time"></div>
      <div class="stamp-row stamp-row--first">
        <span class="stamp"></span><span class="stamp"></span><span class="stamp"></span><span class="stamp"></span><span class="stamp"></span>
        <span class="stamp-row__reward">free treatment</span>
      </div>
      <div class="stamp-row stamp-row--second">
        <span class="stamp"></span><span class="stamp"></span><span class="stamp"></span><span class="stamp"></span><span class="stamp"></span>
        <span class="stamp-row__reward">10% off</span>
      </div>
    </div>
  </section>

  <section class="card card--front" aria-label="Contact details side">
    <svg class="card__art" viewBox="0 0 520 310" preserveAspectRatio="none">
      <defs>
        <radialGradient id="damaskFront" cx="55%" cy="45%" r="60%">
          <stop offset="0" stop-color="var(--damask-light)"/>
          <stop offset="1" stop-color="var(--damask-dark)"/>
        </radialGradient>
      </defs>
      <rect x="0" y="0" width="520" height="310" fill="url(#damaskFront)" role="img" aria-label="Dark vintage damask pattern"/>
      <path d="M0,0 L230,0 C140,0 60,14 0,34 Z" fill="var(--card-black)"/>
      <path d="M0,62 C80,30 180,24 290,24 C330,24 345,0 380,0 L230,0 C140,0 60,14 0,34 Z" fill="var(--silver)"/>
      <path d="M0,300 C60,270 150,262 260,262 C360,262 440,250 520,200 L520,232 C450,280 380,290 300,310 L0,310 Z" fill="var(--silver)"/>
      <path d="M300,310 C380,290 450,280 520,232 L520,310 Z" fill="var(--card-black)"/>
    </svg>
    <div class="card__content">
      <h1 class="brand-name">Parlour 71</h1>
      <div class="contact">
        <p class="contact__name">Mira Dunwoody</p>
        <p class="contact__phone">0431279406</p>
        <p class="contact__address">71 Orchard Crescent, Tallow Bend</p>
      </div>
    </div>
  </section>

</main>
</body>
</html>
```